smart logo for a small painting company located in rainy Vancouver Bc *

I need a logo design for business cards and vehicle signage that will cover the entire work van.
Colors: I am open minded
Its a residential/commercial painting company.
I live in the rain forest of western canada. Raincity Vancouver Bc.
I want something that makes people think of the environment as Precious.
I would like to see designs from conservative to wild and crazy.

Target Market(s)

high end residential/commercial painting

Industry/Entity Type

Painting And Decorating

Contact Information for Business Card

On the Front, Just the logo with the logo text. the card stock should have no white showing.
On the Back: Copper Finch Coatings Company
Owner:Darel Hunsaker
Phone:604 318 2465
Email:copperfinchcoatings@mailvista.net
Fully insured, Clean, Quality Service.

Logo Text

Copper Finch Coatings Company

Font styles to use
Other font styles liked:
• Axis

Colors

Designer to choose colors to be used in the design.

Requirements
Must have
• My project must have bold colors.
Nice to have
• A tree frog walking through paint and tracking it up the side of a building
• A tree frog being painted by an artist.
• A paisley tree frog.
Should not have
• A beret. This frog isn't french.

```html
<!DOCTYPE html>
<html lang="en">
<head>
<meta charset="UTF-8">
<title>Copper Finch Coatings Company — Business Card</title>
<link rel="stylesheet" href="https://fonts.googleapis.com/css2?family=Oswald:wght@600&family=Questrial&display=swap">
<style>
  :root {
    --page: #ffffff;
    --card: #101a12;
    --ink: #ffffff;
    --rule: #cfd3cf;
    --accent: #e06d26;
  }
  * { margin: 0; padding: 0; box-sizing: border-box; }
  html, body { width: 1200px; height: 1200px; overflow: hidden; background: var(--page); }
  .sheet { position: relative; width: 1200px; height: 1200px; }
  .card {
    position: absolute; top: 445px; width: 538px; height: 310px;
    background: var(--card); color: var(--ink);
    font-family: "Questrial", "Helvetica Neue", Arial, sans-serif;
  }
  .card-front { left: 45px; }
  .card-back { left: 613px; }

  .brand-mark {
    position: absolute; left: 207px; top: 54px; width: 124px; height: 124px;
    border-radius: 50%; background: var(--accent);
  }
  .brand-name {
    position: absolute; left: 0; right: 0; top: 206px; text-align: center;
    font-size: 19px; letter-spacing: 0.32em; line-height: 1.45; text-transform: uppercase;
    color: var(--ink);
  }

  .owner-name {
    position: absolute; left: 0; right: 0; top: 52px; text-align: center;
    font-family: "Oswald", "Arial Narrow", sans-serif; font-weight: 600;
    font-size: 21px; letter-spacing: 0.42em; text-transform: uppercase;
  }
  .owner-rule {
    position: absolute; left: 128px; width: 284px; top: 81px; height: 1px; background: var(--rule);
  }
  .owner-role {
    position: absolute; left: 0; right: 0; top: 89px; text-align: center;
    font-size: 12px; letter-spacing: 0.4em;
  }
  .tagline {
    position: absolute; left: 0; right: 0; top: 163px; text-align: center;
    font-size: 12px; letter-spacing: 0.45em;
  }
  .contact {
    position: absolute; left: 0; right: 0; top: 252px; text-align: center;
    font-size: 11.5px; letter-spacing: 0.42em; line-height: 26px;
  }
</style>
</head>
<body>
  <main class="sheet">
    <section class="card card-front" aria-label="Card front">
      <div class="brand-mark"></div>
      <p class="brand-name">Copper Finch<br>Coatings Company</p>
    </section>

    <section class="card card-back" aria-label="Card back">
      <h1 class="owner-name">Darel Hunsaker</h1>
      <div class="owner-rule"></div>
      <p class="owner-role">OWNER</p>
      <p class="tagline">Fully insured, Clean, Quality Service</p>
      <p class="contact">
        <span class="phone">604 318 2465</span><br>
        <span class="email">copperfinchcoatings@mailvista.net</span>
      </p>
    </section>
  </main>
</body>
</html>
```